A new website for Electrical Contractor Business

We are looking for a unique and new WordPress website design which would include 5 Pages - Home Page, Meet the Team, Our Services, Our Projects and Contact Us page.

The global theme for the website needs to be professional but simple to navigate as we cater for both business and home owner customers.

Our core business service is targeted around lighting from single room decorative to large office so the theme should incorporate this in some way.

The home page should include;
Our business logo, Contact number, Email address, small Image rotation box - Highlighting pervious projectsText box - With welcome message, News Feed news reel/Customer feed back box.

I would also like to see a 2 boxes for the separate customer types we services. Business and Home Owner. each box will have a small image with a small text description with a link to the area of the services page relevant to that customer type.

Meet the team page -This will be introducing potential customers to the team so I would like it to include for each team member. Something like a small image and text area which will introduce an outline of the team members skills and abilities.

Our Services page This page will be outlining the different services on offer to the both customer types business and homeowner. Each service should have an image with text description of the service would good here.

Our projects page-Will include images of pervious projects and work we have completed along with a text area for the project description/ outliner.

Contact Us page - Should include a contact form which should include an option for the customer to quest us to call them back, also a selection box for them to inform us our how they found our details would be good.

Colour - The theme colours can be taken from the logo or feel free to impress with your own imagination.

Remember we are looking for a website that will interest our customers enough to except our services or be drawn further into the website.. So call to action links to other areas of the site/ contact page are welcome

Target Market(s)

Business - Office, warehousing and Large Store - lighting and Power
Home owner lighting and power

Coding

Coded - Design and coding required

Number of Pages Required

5+ page

Font styles to use
Serif
Sans Serif

Colors

Designer to choose colors to be used in the design.

Requirements
Must have
• Logo integrated into the website design - i.e. website colours which allow the logo to blend into the design.
Nice to have
• Custom but professional theme catering to business customers, but also show that we do provide services to home owners too.
Should not have
• Sorry am not interested in one oversized block image on rotation covering half the home page.. Images will be needed but not a single block over sized frame with not text, shape. Please use your imagination when considering this design

```html
<!DOCTYPE html>
<html lang="en">
<head>
<meta charset="utf-8">
<title>Voltline – Electrical Services</title>
<link href="https://fonts.googleapis.com/css2?family=Montserrat:wght@500;600;700;800&family=Lato:ital,wght@0,400;0,700;1,400&display=swap" rel="stylesheet">
<style>
:root{
  --navy:#1b2d78;
  --navy-deep:#0f1f66;
  --orange:#f26722;
  --orange-soft:#f7844a;
  --ink:#2b2b2b;
  --muted:#8a8a8a;
  --line:#e4e4e4;
  --paper:#ffffff;
  --mist:#f5f5f7;
  --head:'Montserrat',Arial,sans-serif;
  --body:'Lato',Arial,sans-serif;
}
*{box-sizing:border-box;margin:0;padding:0}
html,body{width:1200px;height:4358px;overflow:hidden}
body{font-family:var(--body);color:var(--ink);background:var(--paper);position:relative}
section,header,footer{position:absolute;left:0;width:1200px}
.abs{position:absolute}
.btn{display:inline-block;background:var(--orange);color:#fff;font-family:var(--body);font-size:15px;padding:13px 26px;border-radius:2px}
.btn-navy{background:var(--navy)}
.section-title{position:absolute;left:0;width:1200px;text-align:center;font-family:var(--head);font-weight:700;font-size:31px;letter-spacing:2px;text-transform:uppercase;color:var(--navy)}
.section-title span{color:var(--orange)}
.section-sub{position:absolute;left:0;width:1200px;text-align:center;font-style:italic;font-size:16px;color:var(--muted)}

/* header */
.site-header{top:0;height:110px;background:#fff;box-shadow:0 2px 8px rgba(0,0,0,.06);z-index:3}
.topbar-phone,.topbar-mail{position:absolute;top:0;height:28px;color:#fff;font-size:13px;font-weight:700;display:flex;align-items:center;gap:8px;padding:0 20px}
.topbar-phone{left:686px;width:174px;background:var(--navy);border-bottom-left-radius:14px}
.topbar-mail{left:860px;width:200px;background:var(--orange);border-bottom-right-radius:14px}
.brand{position:absolute;left:151px;top:24px;display:flex;align-items:center;gap:12px}
.brand-dot{width:52px;height:52px;border-radius:50%;background:var(--orange)}
.brand-name{font-family:var(--head);font-weight:700;font-size:26px;color:var(--navy);letter-spacing:1px;text-transform:uppercase}
.main-nav{position:absolute;left:532px;top:54px;display:flex;gap:36px}
.main-nav a{font-family:var(--head);font-weight:600;font-size:13px;color:var(--navy);text-transform:uppercase;text-decoration:none}

/* hero */
.hero{top:110px;height:297px;background:linear-gradient(90deg,#2a2a2e 0%,#3b3c42 45%,#5d5e66 70%,#44454b 100%)}
.hero-figure{position:absolute;left:700px;top:0;width:320px;height:297px;background:linear-gradient(180deg,#f3a14a 0%,#3a5aa8 55%,#2a3d7a 100%);opacity:.85}
.hero h1{position:absolute;left:151px;top:80px;font-family:var(--head);font-weight:700;font-size:31px;line-height:42px;color:#fff}
.hero .btn{position:absolute;left:151px;top:180px}

/* welcome */
.welcome{top:407px;height:503px}
.welcome .section-title{top:82px}
.welcome .section-sub{top:140px}
.welcome h2{position:absolute;left:151px;top:200px;font-family:var(--head);font-weight:700;font-size:20px;color:var(--navy)}
.welcome p.lead{position:absolute;left:151px;top:240px;width:460px;font-size:16px;line-height:25px;color:#444}
.welcome .btn{position:absolute;left:151px;top:386px}
.welcome .call{position:absolute;left:390px;top:398px;color:var(--orange);font-size:16px;display:flex;gap:8px;align-items:center}
.team-photo{position:absolute;left:616px;top:160px;width:465px;height:343px;background:linear-gradient(180deg,#f4f1ea 0%,#e9c45a 30%,#8a6a3a 70%,#5b4a35 100%)}

/* audiences */
.audiences{top:910px;height:375px;display:flex}
.audience{position:relative;width:600px;height:375px;text-align:center;color:#fff}
.audience.business{background:linear-gradient(135deg,#223a8f,#1b2d78 60%,#15246a)}
.audience.home{background:linear-gradient(135deg,#f7874c,#f26722 60%,#e25a16)}
.audience .icon{position:absolute;left:270px;top:60px}
.audience h3{position:absolute;left:0;width:600px;top:148px;font-family:var(--head);font-weight:600;font-size:27px;letter-spacing:2px;text-transform:uppercase}
.audience p{position:absolute;left:140px;width:320px;top:190px;font-size:15px;line-height:20px}
.audience .btn{position:absolute;left:240px;top:288px;padding:10px 22px}

/* projects */
.projects{top:1285px;height:740px}
.projects .section-title{top:86px}
.projects .section-sub{top:136px}
.filters{position:absolute;top:194px;left:262px;display:flex;gap:34px;align-items:center}
.filters span{font-family:var(--head);font-size:13px;font-weight:600;text-transform:uppercase;color:#333}
.filters .active{background:var(--orange);color:#fff;padding:9px 18px;border-radius:3px}
.grid{position:absolute;top:278px;left:0;width:1200px;height:462px;display:grid;grid-template-columns:repeat(4,300px);grid-template-rows:repeat(2,231px)}
.tile{position:relative}
.t1{background:linear-gradient(135deg,#3b4a66,#1f2a3f)}
.t2{background:linear-gradient(135deg,#4a4036,#2d2520)}
.t3{background:linear-gradient(135deg,#8a6a4c,#3e3630)}
.t4{background:linear-gradient(135deg,#f2a24a,#b35f2a)}
.t5{background:linear-gradient(135deg,#25324a,#c89a3a)}
.t6{background:linear-gradient(135deg,#e8d26a,#9a8060)}
.t7{background:linear-gradient(135deg,#3a3a44,#7a6a5a)}
.t8{background:linear-gradient(135deg,#f0c43a,#5a7aa8)}
.tile-card{position:absolute;left:20px;top:14px;width:260px;height:204px;background:rgba(20,20,24,.72);color:#fff;text-align:center;padding-top:60px}
.tile-card h4{font-family:var(--head);font-size:18px;font-weight:600}
.tile-card p{font-size:13px;line-height:18px;color:#ddd;margin:14px 30px 0}

/* team */
.team{top:2025px;height:634px}
.team .section-title{top:86px}
.team .section-sub{top:136px}
.member{position:absolute;top:184px;width:200px;height:363px}
.m1{left:160px;background:linear-gradient(180deg,#c9a27a,#7a5a3a 50%,#3a3a3a)}
.m2{left:378px;background:linear-gradient(180deg,#f0c430,#1c2a5a 45%,#2a3550)}
.m3{left:610px;background:linear-gradient(180deg,#f28a30,#4a6aa8 45%,#2a3a6a)}
.m4{left:842px;background:linear-gradient(180deg,#f0c430,#22305e 40%,#1a2450)}
.member-card{position:absolute;left:378px;top:387px;width:218px;height:160px;background:var(--orange);color:#fff;text-align:center;border-top-right-radius:40px;padding-top:44px}
.member-card h4{font-family:var(--head);font-size:19px;font-weight:600}
.member-card p{font-size:14px;margin-top:4px}
.member-card .social{display:flex;gap:12px;justify-content:center;margin-top:16px}
.member-card .social i{width:14px;height:14px;border-radius:50%;background:#fff;display:block}

/* stats */
.stats{top:2659px;height:203px;background:linear-gradient(120deg,#1b2d78,#26409a 50%,#1b2d78)}
.stat{position:absolute;top:62px;display:flex;gap:16px;color:#fff}
.stat b{font-family:var(--head);font-size:30px;font-weight:700;display:block;line-height:32px}
.stat small{font-size:14px;text-transform:uppercase;letter-spacing:.5px;display:block;margin-top:10px}

/* testimonials */
.customers{top:2862px;height:619px}
.customers .section-title{top:80px}
.customers .section-sub{top:132px}
.quote-card{position:absolute;top:190px;width:276px;height:320px;background:#fff;border:1px solid var(--line);text-align:center;padding-top:30px}
.quote-card.raised{top:180px;box-shadow:0 16px 30px rgba(242,103,34,.22);border-color:#f3e3d8}
.avatar{width:72px;height:72px;border-radius:50%;margin:0 auto;background:linear-gradient(135deg,#d9b99a,#8a6a52)}
.quote-card h4{font-family:var(--head);font-size:17px;font-weight:600;color:var(--navy);margin-top:18px}
.quote-card .role{color:var(--orange);font-size:14px;margin-top:4px}
.quote-card .mark{font-family:Georgia,serif;font-size:44px;line-height:30px;color:#ccc;margin-top:14px}
.quote-card p{font-style:italic;font-size:14px;line-height:22px;color:#666;margin:8px 32px 0}
.arrow{position:absolute;color:var(--orange)}

/* feed */
.feed{top:3481px;height:524px;background:var(--mist)}
.feed .section-title{top:110px}
.feed .section-sub{top:162px}
.post{position:absolute;top:218px;width:276px;height:189px;background:#fff;padding:22px 22px}
.post-head{display:flex;gap:12px;align-items:center}
.post-head .avatar{width:38px;height:38px;margin:0}
.post-head h5{font-size:13px;font-weight:700;color:var(--navy)}
.post-head span{font-size:11px;color:var(--muted)}
.post .badge{position:absolute;right:22px;top:22px;width:14px;height:14px;border-radius:50%;background:#3a9bdc}
.post p{font-size:13px;line-height:20px;color:#555;margin-top:16px}
.post .date{position:absolute;right:22px;bottom:16px;font-size:11px;color:var(--muted)}

/* footer */
.site-footer{top:4005px;height:353px;background:var(--navy-deep);color:#fff}
.site-footer .brand{top:60px}
.site-footer .brand-dot{width:40px;height:40px}
.site-footer .brand-name{color:#fff;font-size:22px}
.foot-about{position:absolute;left:151px;top:126px;width:300px;font-size:14px;line-height:22px;color:#dfe3f3}
.foot-col{position:absolute;top:78px}
.foot-col h6{font-family:var(--head);font-size:15px;font-weight:600;text-transform:uppercase;letter-spacing:1px;margin-bottom:22px}
.foot-col li{list-style:none;font-size:14px;line-height:27px;color:#dfe3f3;display:flex;gap:10px;align-items:flex-start}
.foot-col li i{width:12px;height:12px;border-radius:50%;background:var(--orange);display:block;margin-top:7px;flex:none}
.foot-rule{position:absolute;left:151px;top:268px;width:898px;height:1px;background:rgba(255,255,255,.2)}
.foot-copy{position:absolute;left:151px;top:290px;font-size:13px;color:#dfe3f3}
.foot-legal{position:absolute;left:815px;top:290px;font-size:13px;color:#dfe3f3}
</style>
</head>
<body>

<header class="site-header">
  <div class="topbar-phone">
    <svg width="12" height="12" viewBox="0 0 24 24"><path d="M6.6 10.8a15.1 15.1 0 0 0 6.6 6.6l2.2-2.2a1 1 0 0 1 1-.25 11.4 11.4 0 0 0 3.6.6 1 1 0 0 1 1 1V20a1 1 0 0 1-1 1A17 17 0 0 1 3 4a1 1 0 0 1 1-1h3.5a1 1 0 0 1 1 1c0 1.25.2 2.45.6 3.6a1 1 0 0 1-.25 1z" fill="#fff"/></svg>
    1 (800) 555-0147
  </div>
  <div class="topbar-mail">
    <svg width="13" height="10" viewBox="0 0 26 20"><rect x="1" y="1" width="24" height="18" fill="none" stroke="#fff" stroke-width="2"/><path d="M1 1l12 10L25 1" fill="none" stroke="#fff" stroke-width="2"/></svg>
    info@voltlinetech.com
  </div>
  <div class="brand"><span class="brand-dot"></span><span class="brand-name">Voltline</span></div>
  <nav class="main-nav">
    <a>Home</a><a>Meet the Team</a><a>Our Services</a><a>Projects</a><a>Contact Us</a>
  </nav>
</header>

<section class="hero" role="img" aria-label="Electrical switch room background with a smiling electrician holding a toolbox">
  <div class="hero-figure" role="img" aria-label="Electrician in hard hat and overalls carrying a toolbox"></div>
  <h1>Best electrical services<br>with perfect repairs</h1>
  <span class="btn">Make an Appoiment</span>
</section>

<section class="welcome">
  <h2 class="section-title">Welcome to <span>Voltline</span></h2>
  <p class="section-sub">Lorem ipsum dolor sit amet, consectetuer adipiscing elit, sed diam nonummy</p>
  <h2>We are shockingly good at what we do</h2>
  <p class="lead">Lorem ipsum dolor sit amet, consectetuer adipiscing elit, sed diam nonummy nibh euismod tincidunt laoreet dolore volutpat. Ut wisi enim ad minim veniam, quis nostrud exerci tation ullamcorper suscipit</p>
  <span class="btn">Make an Appoiment</span>
  <span class="call">
    <svg width="14" height="14" viewBox="0 0 24 24"><path d="M6.6 10.8a15.1 15.1 0 0 0 6.6 6.6l2.2-2.2a1 1 0 0 1 1-.25 11.4 11.4 0 0 0 3.6.6 1 1 0 0 1 1 1V20a1 1 0 0 1-1 1A17 17 0 0 1 3 4a1 1 0 0 1 1-1h3.5a1 1 0 0 1 1 1c0 1.25.2 2.45.6 3.6a1 1 0 0 1-.25 1z" fill="#f26722"/></svg>
    1 (800) 555-0147
  </span>
  <div class="team-photo" role="img" aria-label="Three electricians in yellow hard hats with tool belts"></div>
</section>

<section class="audiences">
  <div class="audience business" role="group" aria-label="Business customers">
    <svg class="icon" width="60" height="60" viewBox="0 0 60 60"><g fill="#fff"><rect x="14" y="20" width="14" height="34"/><rect x="30" y="8" width="16" height="46"/><rect x="8" y="54" width="44" height="3"/></g><g fill="#1b2d78"><rect x="34" y="14" width="3" height="4"/><rect x="40" y="14" width="3" height="4"/><rect x="34" y="24" width="3" height="4"/><rect x="40" y="24" width="3" height="4"/><rect x="34" y="34" width="3" height="4"/><rect x="40" y="34" width="3" height="4"/><rect x="18" y="28" width="3" height="4"/><rect x="18" y="38" width="3" height="4"/></g></svg>
    <h3>Business</h3>
    <p>Lorem ipsum dolor consectetuer adipiscing elit, sed diam nonummy nibh euismod tincidunt laoreet dolore volutpat, wisi enim ad minim veniam</p>
    <span class="btn">Read More</span>
  </div>
  <div class="audience home" role="group" aria-label="Home owner customers">
    <svg class="icon" width="60" height="60" viewBox="0 0 60 60"><path d="M30 8L6 28h6v24h36V28h6z" fill="#fff"/><rect x="25" y="36" width="10" height="16" fill="#f26722"/><rect x="17" y="33" width="6" height="6" fill="#f26722"/><rect x="37" y="33" width="6" height="6" fill="#f26722"/></svg>
    <h3>Home Owner</h3>
    <p>Lorem ipsum dolor consectetuer adipiscing elit, sed diam nonummy nibh euismod tincidunt laoreet dolore volutpat, wisi enim ad minim veniam</p>
    <span class="btn btn-navy">Read More</span>
  </div>
</section>

<section class="projects">
  <h2 class="section-title">Latest <span>Projects</span></h2>
  <p class="section-sub">Lorem ipsum dolor sit amet, consectetuer adipiscing elit, sed diam nonummy</p>
  <div class="filters">
    <span class="active">All Projects</span><span>Electrical Design</span><span>Installation</span><span>Interior</span><span>Lighting</span>
  </div>
  <div class="grid">
    <div class="tile t1" role="img" aria-label="Electricians working on a distribution board"></div>
    <div class="tile t2" role="img" aria-label="Technician testing an electrical panel">
      <div class="tile-card"><h4>Electrical Testing</h4><p>Lorem ipsum consectetuer adipiscing diam nonummy nibh euismod</p></div>
    </div>
    <div class="tile t3" role="img" aria-label="Electrician wiring an overhead fitting"></div>
    <div class="tile t4" role="img" aria-label="Smiling electrician in a hard hat"></div>
    <div class="tile t5" role="img" aria-label="Electrician wearing a protective mask at a panel"></div>
    <div class="tile t6" role="img" aria-label="Electrician in yellow helmet connecting cables"></div>
    <div class="tile t7" role="img" aria-label="Worker installing a light fitting"></div>
    <div class="tile t8" role="img" aria-label="Electrician checking a control cabinet"></div>
  </div>
</section>

<section class="team">
  <h2 class="section-title">Meet <span>The Team</span></h2>
  <p class="section-sub">Lorem ipsum dolor sit amet, consectetuer adipiscing elit, sed diam nonummy</p>
  <div class="member m1" role="img" aria-label="Team member with cable coil and tool belt"></div>
  <div class="member m2" role="img" aria-label="Team member in yellow hard hat"></div>
  <div class="member m3" role="img" aria-label="Team member in orange hard hat and plaid shirt"></div>
  <div class="member m4" role="img" aria-label="Team member in navy overalls and yellow hard hat"></div>
  <div class="member-card">
    <h4>Dana Whitcombe</h4>
    <p>Electrician</p>
    <div class="social"><i></i><i></i><i></i><i></i><i></i></div>
  </div>
</section>

<section class="stats">
  <div class="stat" style="left:151px">
    <svg width="46" height="46" viewBox="0 0 46 46" fill="none" stroke="#fff" stroke-width="3"><path d="M8 38L30 16"/><circle cx="34" cy="12" r="7"/><path d="M8 8l14 14M6 12l6-6"/><path d="M26 30l10 10"/></svg>
    <div><b>30</b><small>Contries Reached</small></div>
  </div>
  <div class="stat" style="left:392px">
    <svg width="46" height="46" viewBox="0 0 46 46" fill="none" stroke="#fff" stroke-width="3"><rect x="5" y="14" width="36" height="26"/><path d="M16 14V8h14v6M5 24h36"/></svg>
    <div><b>64</b><small>Site Inspection</small></div>
  </div>
  <div class="stat" style="left:625px">
    <svg width="46" height="46" viewBox="0 0 46 46" fill="none" stroke="#fff" stroke-width="3"><rect x="10" y="4" width="26" height="38"/><path d="M16 14h14M16 22h14M16 30h10M6 8v34"/></svg>
    <div><b>272</b><small>Project Done</small></div>
  </div>
  <div class="stat" style="left:863px">
    <svg width="46" height="46" viewBox="0 0 46 46" fill="none" stroke="#fff" stroke-width="3"><circle cx="23" cy="14" r="9"/><path d="M6 42c0-10 8-16 17-16s17 6 17 16"/></svg>
    <div><b>60</b><small>Qualified Staff</small></div>
  </div>
</section>

<section class="customers">
  <h2 class="section-title">Happy <span>Customers</span></h2>
  <p class="section-sub">Lorem ipsum dolor sit amet, consectetuer adipiscing elit, sed diam nonummy</p>
  <svg class="arrow" style="left:96px;top:340px" width="14" height="24" viewBox="0 0 14 24"><path d="M12 2L2 12l10 10" fill="none" stroke="#555" stroke-width="2.5"/></svg>
  <div class="quote-card" style="left:151px">
    <div class="avatar" role="img" aria-label="Customer portrait"></div>
    <h4>Marcus Ellery</h4><div class="role">Site Manager</div><div class="mark">“</div>
    <p>“ Lorem ipsum dolor consectetuer adipiscing elit nonummy nibh euismod tincidunt laoreet dolore volutpat wisi enim ad minim veniam”</p>
  </div>
  <div class="quote-card raised" style="left:459px">
    <div class="avatar" role="img" aria-label="Customer portrait"></div>
    <h4>Ivo Santner</h4><div class="role">Site Manager</div><div class="mark">“</div>
    <p>“ Lorem ipsum dolor consectetuer adipiscing elit nonummy nibh euismod tincidunt laoreet dolore volutpat wisi enim ad minim veniam”</p>
  </div>
  <div class="quote-card" style="left:770px">
    <div class="avatar" role="img" aria-label="Customer portrait"></div>
    <h4>Lena Hartwell</h4><div class="role">Site Manager</div><div class="mark">“</div>
    <p>“ Lorem ipsum dolor consectetuer adipiscing elit nonummy nibh euismod tincidunt laoreet dolore volutpat wisi enim ad minim veniam”</p>
  </div>
  <svg class="arrow" style="left:1086px;top:340px" width="14" height="24" viewBox="0 0 14 24"><path d="M2 2l10 10L2 22" fill="none" stroke="#f26722" stroke-width="2.5"/></svg>
</section>

<section class="feed">
  <h2 class="section-title">News <span>Feed</span></h2>
  <p class="section-sub">Lorem ipsum dolor sit amet, consectetuer adipiscing elit, sed diam nonummy</p>
  <svg class="arrow" style="left:96px;top:302px" width="14" height="24" viewBox="0 0 14 24"><path d="M12 2L2 12l10 10" fill="none" stroke="#555" stroke-width="2.5"/></svg>
  <article class="post" style="left:151px">
    <div class="post-head"><div class="avatar" role="img" aria-label="Author portrait"></div><div><h5>Tomas Reyland</h5><span>@tomasreyland</span></div></div>
    <span class="badge"></span>
    <p>Lorem ipsum sectetuer adipiscing elitwisi nonummy euismod tincidunt laoreet dolore volutpat wisi volutpenim</p>
    <span class="date">Apr 21</span>
  </article>
  <article class="post" style="left:459px">
    <div class="post-head"><div class="avatar" role="img" aria-label="Author portrait"></div><div><h5>Tomas Reyland</h5><span>@tomasreyland</span></div></div>
    <span class="badge"></span>
    <p>Lorem ipsum sectetuer adipiscing elitwisi nonummy euismod tincidunt laoreet dolore volutpat wisi volutpenim</p>
    <span class="date">Apr 21</span>
  </article>
  <article class="post" style="left:770px">
    <div class="post-head"><div class="avatar" role="img" aria-label="Author portrait"></div><div><h5>Tomas Reyland</h5><span>@tomasreyland</span></div></div>
    <span class="badge"></span>
    <p>Lorem ipsum sectetuer adipiscing elitwisi nonummy euismod tincidunt laoreet dolore volutpat wisi volutpenim</p>
    <span class="date">Apr 21</span>
  </article>
  <svg class="arrow" style="left:1086px;top:302px" width="14" height="24" viewBox="0 0 14 24"><path d="M2 2l10 10L2 22" fill="none" stroke="#f26722" stroke-width="2.5"/></svg>
</section>

<footer class="site-footer">
  <div class="brand"><span class="brand-dot"></span><span class="brand-name">Voltline</span></div>
  <p class="foot-about">Lorem ipsum dolor sit amet conctetuer adipiscing elit diam nonummy ni euismod tincidunt laoreet dolore volutpat. wisi enim ad minim veniam, quis nostrud exerci tation suscipit</p>
  <div class="foot-col" style="left:505px">
    <h6>Quick Links</h6>
    <ul><li>Home</li><li>Meet The Team</li><li>Our Services</li><li>Projects</li><li>Contact Us</li></ul>
  </div>
  <div class="foot-col" style="left:697px">
    <h6>Quick Links</h6>
    <ul>
      <li><i></i>1280 Beacon Row<br>Harbour City, NA, 20411</li>
      <li><i></i>1 (800) 555-0147</li>
      <li><i></i>info@voltlinetech.com</li>
    </ul>
  </div>
  <div class="foot-col" style="left:936px">
    <h6>Follow Us</h6>
    <ul><li><i></i>Community</li><li><i></i>News Feed</li><li><i></i>Gallery</li></ul>
  </div>
  <div class="foot-rule"></div>
  <p class="foot-copy">Copyrights © 2017 Voltline. All Rights Reserved</p>
  <p class="foot-legal">Privacy Policy &nbsp;|&nbsp; Terms &amp; Conditions</p>
</footer>

</body>
</html>
```